QuorraLink Business Card

We require a stunning business card for QuorraLink - a new digital marketing agency. The logo provided was designed by a graphic designer here on ArtHivePro.

www.quorralink-example.net - "Get more sales online"

What we do:
The business delivers website optimisation (Web design, social media strategy, digital strategies, SEO, PPC, conversion optimisation, email marketing) to get businesses more sales online.

The card must match the brand style which can be found on this website template:

http://layoutbazaar.example/item/plumline-adaptive-allpurpose-skin/full_screen_preview/7193046

It must have 'wow' factor so that you'll never forget QuorraLink - We're open to any materials, textures you think will work.

We don't want a boring run of the mill design - I can knock that up in Photoshop myself or use a template solution. It should be timeless and only need replacing should the contact details change.

The design should be eye catching, future proof, exceptionally chic, classy and oozing authority and confidence. QuorraLink services must not look cheap.

Here's some brilliant designs to point you in the right direction:

http://tidycraftz.example/30-superb-calling-cards/

The spec is for double sided, but we're open to your ideas. If it's going on an opaque or see through card, then of course a single side is preferable. Using creativity and thought on the medium for the card - shape - texture is desirable.

The strapline for the business is "Get more business online" please submit with / without strapline.
Updates

Please only submit your best 1-3 designs initially.

Target Market(s)

Business 2 Business - Local SMEs
Local professionals - Doctors, Dentists, Financials, Bespoke Retailers, Property companies - anyone with a decent budget to spend on digital marketing services and a high margin product or service to sell.

Industry/Entity Type

Graphic Designer

Requirements
Must have
• Text:
• name: Tom Walcroft
• position Digital Marketing Director
• mobile 07911 204 658
• website www.quorralink-example.net
Nice to have
• Check See http://tidycraftz.example/30-superb-calling-cards/ for ideas.
• LinkedIn and Twitter usernames if there is space and it works on the design.

```html
<!DOCTYPE html>
<html lang="en">
<head>
<meta charset="utf-8">
<title>QuorraLink Business Card</title>
<link href="https://fonts.googleapis.com/css2?family=Questrial&display=swap" rel="stylesheet">
<style>
  :root {
    --page-bg: #ecebe8;
    --card-white: #ffffff;
    --brand-red: #e8402b;
    --brand-navy: #1e4a5c;
    --card-shadow: rgba(30, 40, 50, 0.18);
  }
  * { box-sizing: border-box; margin: 0; padding: 0; }
  html, body {
    width: 1200px;
    height: 646px;
    overflow: hidden;
    background: var(--page-bg);
    font-family: "Questrial", sans-serif;
  }
  .sheet {
    position: relative;
    width: 1200px;
    height: 646px;
  }
  .card {
    position: absolute;
    top: 173px;
    width: 520px;
    height: 300px;
    background: var(--card-white);
    box-shadow: 0 6px 18px var(--card-shadow);
    overflow: hidden;
  }
  .card--front { left: 50px; }
  .card--back { left: 630px; }

  /* Front side */
  .brand {
    position: absolute;
    top: 52px;
    left: 0;
    right: 0;
    text-align: center;
  }
  .brand__lockup {
    display: inline-flex;
    align-items: center;
    gap: 12px;
  }
  .brand__dot {
    width: 30px;
    height: 30px;
    border-radius: 50%;
    background: var(--brand-red);
  }
  .brand__name {
    font-size: 50px;
    line-height: 1;
    color: var(--brand-navy);
    letter-spacing: 0.5px;
  }
  .brand__tagline {
    margin-top: 8px;
    font-size: 13px;
    color: var(--brand-navy);
  }
  .rule {
    position: absolute;
    left: 70px;
    right: 70px;
    height: 2px;
    background: var(--brand-navy);
  }
  .rule--top { top: 160px; }
  .rule--bottom { top: 232px; }
  .front__strap {
    position: absolute;
    top: 182px;
    left: 0;
    right: 0;
    text-align: center;
    font-size: 20px;
    color: var(--brand-navy);
  }

  /* Back side */
  .back__band {
    position: absolute;
    top: 0;
    bottom: 0;
    left: 190px;
    width: 34px;
    background: var(--brand-navy);
  }
  .back__panel {
    position: absolute;
    top: 0;
    bottom: 0;
    left: 224px;
    right: 0;
    background: var(--brand-red);
    color: var(--brand-navy);
  }
  .person {
    position: absolute;
    top: 22px;
    right: 22px;
    text-align: right;
  }
  .person__name { font-size: 14px; letter-spacing: 0.5px; text-transform: uppercase; }
  .person__role { font-size: 12px; margin-top: 2px; }
  .contacts {
    position: absolute;
    left: 18px;
    top: 150px;
    list-style: none;
  }
  .contacts__item {
    display: flex;
    align-items: center;
    gap: 10px;
    font-size: 13px;
    margin-bottom: 10px;
  }
  .contacts__icon { width: 15px; height: 15px; flex: none; }
  .back__tagline {
    position: absolute;
    left: 18px;
    right: 18px;
    bottom: 22px;
    font-size: 13px;
    white-space: nowrap;
  }
</style>
</head>
<body>
<main class="sheet">

  <section class="card card--front" aria-label="Card front">
    <div class="brand">
      <div class="brand__lockup">
        <span class="brand__dot"></span>
        <span class="brand__name">QuorraLink</span>
      </div>
      <p class="brand__tagline">Visibility on the internet for business websites</p>
    </div>
    <div class="rule rule--top"></div>
    <p class="front__strap">www.quorralink-example.net - "Get more sales online"</p>
    <div class="rule rule--bottom"></div>
  </section>

  <section class="card card--back" aria-label="Card back">
    <div class="back__band"></div>
    <div class="back__panel">
      <div class="person">
        <p class="person__name">Tom Walcroft</p>
        <p class="person__role">Digital Marketing Director</p>
      </div>
      <ul class="contacts">
        <li class="contacts__item">
          <svg class="contacts__icon" viewBox="0 0 16 16" aria-hidden="true">
            <path fill="#1e4a5c" d="M3 1h3l1.5 4-2 1.2a9 9 0 0 0 4.3 4.3L11 8.5l4 1.5v3a2 2 0 0 1-2 2A12 12 0 0 1 1 3a2 2 0 0 1 2-2z"/>
          </svg>
          <span>07911 204 658</span>
        </li>
        <li class="contacts__item">
          <svg class="contacts__icon" viewBox="0 0 16 16" aria-hidden="true">
            <rect x="1" y="3" width="14" height="10" fill="#1e4a5c"/>
            <path d="M1.5 3.5 8 9l6.5-5.5" fill="none" stroke="#e8402b" stroke-width="1.3"/>
          </svg>
          <span>yourmail@quorralink-example.net</span>
        </li>
        <li class="contacts__item">
          <svg class="contacts__icon" viewBox="0 0 16 16" aria-hidden="true">
            <circle cx="8" cy="8" r="7" fill="#1e4a5c"/>
            <path d="M1 8h14M8 1c-3 3.5-3 10.5 0 14M8 1c3 3.5 3 10.5 0 14" fill="none" stroke="#e8402b" stroke-width="1"/>
          </svg>
          <span>www.quorralink-example.net</span>
        </li>
      </ul>
      <p class="back__tagline">Visibility on the internet for business website</p>
    </div>
  </section>

</main>
</body>
</html>
```